Contemporary Media Company with Logo Needs Business Card Design

Need a modern card design for a full service digital media company using the logo included. Also want the info below on the card. Probably list the services on the card back to save space for the front. Want something contemporary to impress prospective clients. You may want to submit both a somewhat more conservative design, and then a more wild one.
General Info: (this phrase need not be on the card)
Tod Parvin
Founder and CEO
949-628-4513
tod@lumavantstudio.example
lumavantstudio.example
Services: (this word need not be on the card)
Content & Experience Strategy
Brand Development
Search Engine Optimization
Website Design
Website Operation
Social Media Integration
Complete Video Solutions
Industry/Entity Type
Business
Contact Information for Business Card
Tod Parvin
Founder and CEO
949-628-4513
tod@lumavantstudio.example
lumavantstudio.example
Brand Development
Website Design
Website Operation
Social Media Integration
Complete Video Solutions
Look and feel

```html
<!DOCTYPE html>
<html lang="en">
<head>
<meta charset="utf-8">
<title>Lumavant Studio – Business Cards</title>
<link rel="stylesheet" href="https://fonts.googleapis.com/css2?family=Montserrat:wght@500&family=Tinos:wght@400;700&family=Arimo:wght@400&display=swap">
<style>
  :root {
    --backdrop: #e9e6e1;
    --card-white: #ffffff;
    --card-black: #231f20;
    --brand-orange: #f0932b;
    --brand-grey: #8a8a8c;
    --contact-grey: #b9b9b9;
    --ink: #111111;
  }
  * { margin: 0; padding: 0; box-sizing: border-box; }
  html, body { width: 1200px; height: 1000px; overflow: hidden; }
  body {
    background: var(--backdrop);
    display: flex;
    flex-direction: column;
    align-items: center;
    justify-content: center;
    gap: 70px;
  }
  .card {
    width: 700px;
    height: 400px;
    display: flex;
    overflow: hidden;
    box-shadow: 0 10px 24px rgba(0,0,0,0.18);
  }
  .panel-white { background: var(--card-white); position: relative; }
  .panel-black { background: var(--card-black); position: relative; flex: 1; }

  /* Front */
  .card-front .panel-white { width: 40%; display: flex; align-items: center; justify-content: center; }
  .mark-square { width: 58px; height: 58px; background: var(--brand-orange); }
  .card-front .panel-black { display: flex; align-items: center; justify-content: center; }
  .wordmark {
    font-family: "Montserrat", sans-serif;
    font-weight: 500;
    color: var(--brand-grey);
    font-size: 38px;
    letter-spacing: 6px;
    text-align: center;
    line-height: 1.25;
  }

  /* Back */
  .card-back .panel-white { width: 45%; display: flex; flex-direction: column; justify-content: center; padding-left: 70px; }
  .person-name {
    font-family: "Tinos", serif;
    font-weight: 700;
    color: var(--brand-orange);
    font-size: 34px;
  }
  .person-title {
    font-family: "Arimo", sans-serif;
    color: var(--ink);
    font-size: 21px;
    margin-top: 4px;
  }
  .card-back .panel-black { display: flex; flex-direction: column; align-items: center; justify-content: center; gap: 12px; }
  .wordmark-small {
    font-family: "Montserrat", sans-serif;
    font-weight: 500;
    color: var(--brand-grey);
    font-size: 20px;
    letter-spacing: 3px;
    margin-bottom: 14px;
  }
  .contact-item { display: flex; flex-direction: column; align-items: center; gap: 6px; }
  .contact-icon { width: 26px; height: 26px; }
  .contact-text {
    font-family: "Tinos", serif;
    color: var(--contact-grey);
    font-size: 17px;
  }
</style>
</head>
<body>
  <section class="card card-front">
    <div class="panel-white"><div class="mark-square"></div></div>
    <div class="panel-black"><div class="wordmark">LUMAVANT<br>STUDIO</div></div>
  </section>

  <section class="card card-back">
    <div class="panel-white">
      <div class="person-name">Tod Parvin</div>
      <div class="person-title">Founder (CEO)</div>
    </div>
    <div class="panel-black">
      <div class="wordmark-small">LUMAVANT STUDIO</div>
      <div class="contact-item">
        <svg class="contact-icon" viewBox="0 0 26 26" aria-hidden="true">
          <circle cx="13" cy="13" r="13" fill="#f0932b"/>
          <rect x="9" y="6" width="8" height="14" rx="1.5" fill="none" stroke="#231f20" stroke-width="1.6"/>
          <line x1="11.5" y1="17.5" x2="14.5" y2="17.5" stroke="#231f20" stroke-width="1.4"/>
        </svg>
        <span class="contact-text">949-628-4513</span>
      </div>
      <div class="contact-item">
        <svg class="contact-icon" viewBox="0 0 26 26" aria-hidden="true">
          <rect x="2" y="6" width="22" height="14" fill="#f0932b"/>
          <polyline points="2,6 13,14 24,6" fill="none" stroke="#231f20" stroke-width="1.4"/>
        </svg>
        <span class="contact-text">tod@lumavantstudio.example</span>
      </div>
      <div class="contact-item">
        <svg class="contact-icon" viewBox="0 0 26 26" aria-hidden="true">
          <circle cx="13" cy="13" r="12" fill="#f0932b"/>
          <ellipse cx="13" cy="13" rx="5" ry="11" fill="none" stroke="#231f20" stroke-width="1.3"/>
          <line x1="2" y1="13" x2="24" y2="13" stroke="#231f20" stroke-width="1.3"/>
          <line x1="4" y1="8" x2="22" y2="8" stroke="#231f20" stroke-width="1.1"/>
          <line x1="4" y1="18" x2="22" y2="18" stroke="#231f20" stroke-width="1.1"/>
        </svg>
        <span class="contact-text">lumavantstudio.example</span>
      </div>
    </div>
  </section>
</body>
</html>
```